Game like design for my android application

Please take a look at Lumora Staff fundhatch campaign over here: https://www.fundhatch.example/projects/lumorastaff/4820193756/

I need to have a design done for the app. I am not really good in designing stuff as you can see on our fundhatch page. Therefore I don't know whether it should have an antic look or a modern look or a combination of these two.

I would suggest it might have a look similar to the attached file.

But I have no idea and thus I would expect you to come up with ideas. The app is a game-like which involves experience points, achievements, items, battles, medals maybe and such. So I would welcome some knowledge of these kind of things.

Great would be if it could have this Tobin Quell-like look.

Please see this mockup https://sketchvale.example/s/Q2RKD. I just made (please don't stick to that, it should just give you an idea of the application lifecycle, but come up with your own ideas of how those elements should be positioned, how should they look and so on).

Plus see attached logo, maybe the app should keep such color scale.

Hey guys, just a note. Please do not stick to my mock up very much, especially not to the main menu. That menu is there only to display what elements should it have, but I would be happy to see some original user friendly ideas of how that menu could be done. Besides that, thanks a lot for your designs, they look awesome, keep the great work! :)

Games

• Antic-modern gaming look

```html
<!DOCTYPE html>
<html lang="en">
<head>
<meta charset="utf-8">
<title>Lumora Staff – Sign In</title>
<link rel="stylesheet" href="https://fonts.googleapis.com/css2?family=Cormorant+Garamond:wght@400;500&family=Pirata+One&family=Roboto:wght@400&display=swap">
<style>
  :root {
    --sky-deep: #0d1a1c;
    --sky-teal: #2c4a4c;
    --mist: #7c8c6a;
    --moss: #8a8646;
    --earth: #3a3016;
    --soil: #1c170c;
    --ink-light: #e8ecdf;
    --ink-soft: rgba(232, 236, 223, 0.78);
    --field-line: rgba(240, 244, 236, 0.9);
    --button-face: rgba(236, 236, 226, 0.62);
    --button-ink: #3b2016;
    --dot-active: #ffffff;
    --dot-idle: rgba(255, 255, 255, 0.45);
  }
  * { box-sizing: border-box; margin: 0; padding: 0; }
  html, body { width: 677px; height: 1200px; overflow: hidden; background: var(--sky-deep); }
  .screen {
    position: relative; width: 677px; height: 1200px; overflow: hidden;
    font-family: "Cormorant Garamond", Georgia, serif; color: var(--ink-light);
  }
  .backdrop {
    position: absolute; inset: 0;
    background:
      radial-gradient(ellipse 60% 30% at 48% 38%, rgba(200, 210, 180, 0.28), transparent 70%),
      radial-gradient(ellipse 80% 25% at 40% 62%, rgba(190, 180, 110, 0.45), transparent 70%),
      linear-gradient(180deg, var(--sky-deep) 0%, var(--sky-teal) 22%, #4d6656 40%, var(--mist) 52%, var(--moss) 62%, var(--earth) 82%, var(--soil) 100%);
  }
  .next-page-edge {
    position: absolute; top: 40px; right: 0; width: 22px; height: 1080px;
    background: linear-gradient(90deg, rgba(255,255,255,0.05), rgba(220,220,230,0.28));
  }
  .status-bar {
    position: absolute; top: 0; left: 0; right: 0; height: 34px;
    display: flex; align-items: center; justify-content: space-between;
    padding: 0 10px; font-family: "Roboto", Arial, sans-serif; font-size: 22px; color: #fff;
  }
  .status-left { display: flex; align-items: center; gap: 8px; }
  .signal { display: flex; gap: 3px; }
  .signal span { width: 10px; height: 10px; border-radius: 50%; border: 1.5px solid #fff; }
  .signal span.on { background: #fff; }
  .status-time { position: absolute; left: 50%; transform: translateX(-50%); }
  .status-right { display: flex; align-items: center; gap: 8px; }
  .battery { width: 40px; height: 18px; border: 2px solid #fff; border-radius: 3px; padding: 2px; position: relative; }
  .battery::after { content: ""; position: absolute; right: -6px; top: 4px; width: 3px; height: 7px; background: #fff; }
  .battery span { display: block; width: 55%; height: 100%; background: #fff; }

  .field {
    position: absolute; left: 99px; width: 477px; height: 50px;
    border-bottom: 3px solid var(--field-line);
    font-size: 30px; color: var(--ink-soft); line-height: 40px;
  }
  .field-user { top: 347px; }
  .field-pass { top: 442px; }
  .remember {
    position: absolute; top: 550px; left: 191px; display: flex; align-items: center; gap: 22px;
    font-size: 25px; color: var(--ink-light);
  }
  .remember .radio { width: 21px; height: 21px; border: 2px solid var(--ink-light); border-radius: 50%; }
  .forgot {
    position: absolute; top: 605px; left: 0; right: 22px; text-align: center;
    font-size: 25px; color: var(--ink-light); text-decoration: underline;
  }
  .sign-in { position: absolute; left: 190px; top: 788px; width: 312px; height: 148px; }
  .sign-in-label {
    position: absolute; inset: 0; display: flex; align-items: center; justify-content: center;
    font-family: "Pirata One", "Times New Roman", serif; font-size: 62px; color: var(--button-ink);
    padding-bottom: 6px;
  }
  .pager { position: absolute; top: 1141px; left: 316px; display: flex; gap: 18px; }
  .pager span { width: 12px; height: 12px; border-radius: 50%; background: var(--dot-idle); }
  .pager span.active { background: var(--dot-active); }
</style>
</head>
<body>
<main class="screen">
  <div class="backdrop" role="img" aria-label="Misty fantasy backdrop: dark teal sky with swirling magical light fading into golden-green smoky ground"></div>
  <div class="next-page-edge"></div>

  <header class="status-bar">
    <div class="status-left">
      <div class="signal"><span class="on"></span><span class="on"></span><span></span><span></span><span></span></div>
      <span>Telvona</span>
      <svg width="22" height="16" viewBox="0 0 22 16"><path d="M11 15 L2 5 A13 13 0 0 1 20 5 Z" fill="#fff"/></svg>
    </div>
    <span class="status-time">13:18</span>
    <div class="status-right"><span>55 %</span><div class="battery"><span></span></div></div>
  </header>

  <form class="login">
    <div class="field field-user">user name</div>
    <div class="field field-pass">password</div>
    <div class="remember"><span class="radio"></span><span>remember password</span></div>
    <div class="forgot">forgot your password?</div>
    <div class="sign-in">
      <svg width="312" height="148" viewBox="0 0 312 148">
        <polygon points="0,0 312,0 288,148 22,148" fill="var(--button-face)"/>
      </svg>
      <span class="sign-in-label">Sign In</span>
    </div>
  </form>

  <nav class="pager"><span class="active"></span><span></span></nav>
</main>
</body>
</html>
```